Fun & Healthy Dog Treat Business Needs a Business & Loyalty Card

We need a business card design for a business that provides healthy dog products.

The design should communicate a healthy aspect and should communicate that the business focuses on healthy produce.

We would like some aspects if not all of our current logo to appear on the card.

We would also like a two sided card with the back of the card being able to be used as a loyalty program where after purchasing 7 items the buyer receives a free gift. There should be a way of identifying how many purchases a customer has made and if possible enable at least 4 - 5 gives be able to be given on one card. ie make 7 purchases and receive a give, to be able to be done 4 - 5 times before they need to be given a new card.

Rather than the focus be solely on dog treats we would like the card's focus to be a bit wider should we decide to enter other markets in the future and therefore not mention dog treats.

We want the card to be colourful while still retaining a very healthy aspect.

We also need the card to have pictures such as a dog or dogs head that enable us to determine how many items a customer has purchase before we give them a free gift.

Please see our website for further details regarding our business including contact details. www.wrenfieldpantry.com.au

Target Market(s)

Dog lovers who are health concious

Industry/Entity Type

Pet

Contact Information for Business Card

Products for Healthy Dogs
Web Address - www.wrenfieldpantry.com.au
Email address - info@wrenfieldpantry.com.au

Font styles to use
Serif

Colors
acd037
f04a50

Requirements
Must have
• Wrenfield Pantry
• Products for Healthy Dogs
• Web Address - www.wrenfieldpantry.com.au
• Email address - info@wrenfieldpantry.com.au
• Mobile Number - 0417 358 619
Nice to have
• Part of our current logo
• Blend in with current logo but not include the words healthy dog treats
• The flip side of the card should have a Loyalty Program where when you purchase 7 products you receive a free gift.
Should not have
• Should not include the words healthy dog treats
• Should not have the fixed line phone number

```html
<!DOCTYPE html>
<html lang="en">
<head>
<meta charset="utf-8">
<title>Wrenfield Pantry – Business &amp; Loyalty Card</title>
<link rel="stylesheet" href="https://fonts.googleapis.com/css2?family=Merriweather:wght@400;700;900&display=swap">
<style>
  :root {
    --green-light: #cbe56f;
    --green: #acd037;
    --green-deep: #86b92e;
    --red: #f04a50;
    --black: #111111;
    --ink: #1d2a0e;
    --white: #ffffff;
    --backdrop: #e9e9e6;
    --serif: "Merriweather", Georgia, serif;
  }
  * { margin: 0; padding: 0; box-sizing: border-box; }
  html, body {
    width: 1200px; height: 913px; overflow: hidden;
    background: var(--backdrop);
    font-family: var(--serif);
  }
  .canvas { position: relative; width: 1200px; height: 913px; }
  .card {
    position: absolute; width: 620px; height: 354px;
    border-radius: 4px; overflow: hidden;
    box-shadow: 0 10px 28px rgba(0,0,0,.22);
  }
  .card svg.art { position: absolute; inset: 0; }
  .card-front { left: 70px; top: 70px; }
  .card-back { left: 510px; top: 480px; background: var(--white); }

  .brand {
    position: absolute; left: 34px; top: 44px;
    display: flex; align-items: center; gap: 12px;
  }
  .brand-dot { width: 30px; height: 30px; border-radius: 50%; background: var(--red); }
  .brand-name { font-weight: 900; font-size: 30px; color: var(--red); line-height: 38px; }
  .brand-tagline {
    position: absolute; left: 76px; top: 92px;
    font-size: 12px; color: var(--ink); letter-spacing: .5px;
  }
  .person { position: absolute; left: 120px; top: 176px; }
  .person-name { font-weight: 900; font-size: 24px; line-height: 30px; color: var(--ink); letter-spacing: 1px; }
  .person-role { font-size: 12px; line-height: 16px; color: var(--white); letter-spacing: 1.5px; margin-top: 4px; }
  .contact { position: absolute; left: 150px; top: 246px; list-style: none; }
  .contact li {
    display: flex; align-items: center; gap: 10px;
    font-size: 14px; color: var(--ink); line-height: 22px;
  }
  .contact svg { width: 13px; height: 13px; }

  .stamps {
    position: absolute; left: 50%; top: 120px; transform: translateX(-50%);
    display: flex; gap: 14px;
  }
  .stamp {
    width: 52px; height: 52px; border-radius: 50%; background: var(--black);
    display: flex; align-items: center; justify-content: center;
  }
  .stamp-free { background: var(--red); }
  .free-tag {
    background: var(--black); color: var(--white); font-size: 8px; font-weight: 700;
    padding: 5px 4px; border: 1.5px solid var(--white); border-radius: 2px;
  }
  .loyalty-note {
    position: absolute; left: 0; right: 0; top: 192px; text-align: center;
    font-size: 15px; color: var(--ink); line-height: 22px;
  }
  .loyalty-note .gift { color: var(--red); display: block; }
</style>
</head>
<body>
<main class="canvas">

  <section class="card card-front" aria-label="Business card front">
    <svg class="art" viewBox="0 0 620 354" width="620" height="354" aria-hidden="true">
      <defs>
        <linearGradient id="frontGreen" x1="0" y1="0" x2="0.4" y2="1">
          <stop offset="0" stop-color="var(--green-light)"/>
          <stop offset="1" stop-color="var(--green-deep)"/>
        </linearGradient>
      </defs>
      <rect width="620" height="354" fill="url(#frontGreen)"/>
      <path d="M500 0 Q560 170 420 354 L620 354 L620 0 Z" fill="var(--red)"/>
      <path d="M522 0 Q580 175 442 354 L620 354 L620 0 Z" fill="var(--white)"/>
      <path d="M548 0 Q605 180 470 354 L620 354 L620 0 Z" fill="var(--black)"/>
      <line class="name-rule" x1="252" y1="208" x2="498" y2="208" stroke="var(--ink)" stroke-width="1"/>
    </svg>
    <div class="brand">
      <span class="brand-dot"></span>
      <span class="brand-name">Wrenfield Pantry</span>
    </div>
    <p class="brand-tagline">Products for Healthy Dogs</p>
    <div class="person">
      <p class="person-name">MARLA QUINN</p>
      <p class="person-role">OWNER</p>
    </div>
    <ul class="contact">
      <li><svg viewBox="0 0 16 16"><path d="M4 1l3 3-2 2q1 3 5 5l2-2 3 3-2 3Q5 14 1 4Z" fill="var(--ink)"/></svg>0417 358 619</li>
      <li><svg viewBox="0 0 16 16"><rect x="1" y="3" width="14" height="10" fill="none" stroke="var(--ink)" stroke-width="1.5"/><path d="M1 3l7 6 7-6" fill="none" stroke="var(--ink)" stroke-width="1.5"/></svg>info@wrenfieldpantry.com.au</li>
      <li><svg viewBox="0 0 16 16"><circle cx="8" cy="8" r="6.5" fill="none" stroke="var(--ink)" stroke-width="1.5"/><path d="M1.5 8h13M8 1.5q-4 6.5 0 13M8 1.5q4 6.5 0 13" fill="none" stroke="var(--ink)" stroke-width="1.2"/></svg>www.wrenfieldpantry.com.au</li>
    </ul>
  </section>

  <section class="card card-back" aria-label="Loyalty card back">
    <svg class="art" viewBox="0 0 620 354" width="620" height="354" aria-hidden="true">
      <path d="M0 290 Q330 300 620 140 L620 354 L0 354 Z" fill="var(--red)"/>
      <path d="M0 300 Q330 310 620 152 L620 354 L0 354 Z" fill="var(--white)"/>
      <path d="M0 304 Q330 314 620 158 L620 354 L0 354 Z" fill="var(--green)"/>
      <path d="M0 316 Q330 326 620 172 L620 354 L0 354 Z" fill="var(--black)"/>
    </svg>
    <div class="stamps">
      <svg class="stamp-icon" width="0" height="0" aria-hidden="true"><defs><g id="bag"><rect x="3" y="6" width="18" height="15" rx="1.5" fill="var(--white)"/><path d="M3 6l3-4h12l3 4" fill="none" stroke="var(--white)" stroke-width="2"/><rect x="5" y="8" width="14" height="11" fill="var(--black)"/></g></defs></svg>
      <span class="stamp"><svg width="24" height="24" viewBox="0 0 24 24"><use href="#bag"/></svg></span>
      <span class="stamp"><svg width="24" height="24" viewBox="0 0 24 24"><use href="#bag"/></svg></span>
      <span class="stamp"><svg width="24" height="24" viewBox="0 0 24 24"><use href="#bag"/></svg></span>
      <span class="stamp"><svg width="24" height="24" viewBox="0 0 24 24"><use href="#bag"/></svg></span>
      <span class="stamp"><svg width="24" height="24" viewBox="0 0 24 24"><use href="#bag"/></svg></span>
      <span class="stamp"><svg width="24" height="24" viewBox="0 0 24 24"><use href="#bag"/></svg></span>
      <span class="stamp stamp-free"><span class="free-tag">FREE</span></span>
    </div>
    <p class="loyalty-note">When you purchase 7 products you receive a <span class="gift">FREE GIFT</span></p>
  </section>

</main>
</body>
</html>
```